Touch screen based web site design

We have a product called vTrellis.

It is a browser based touch screen application for the apartment leasing industry . You can read more about it at http://vtrellis.korvathsoft.example.

To see how the product functions, you can check the link http://www.webvtrellis.example/vtrellis.aspx?k=demo1.

We have a need to give a new look and feel to the application. The redesign is NOT to be limited to colors and shapes, but an overhaul of the screen layout, color, font scheme to make the application flow nice and smooth. The content of the pages will remain the same.

There will be animations but that can be done by our IT team, if described in concept by the designer.

Again to reiterate, all things are up for grab, do not get influenced by the images, shapes and color used currently.

Reason: None of the design are coming even close to what I am asking for. Please see the homepage of the application at http://www.korvathsoft.example/vtrellis/images/img-screenshot-lg-01.jpg. That is what I am asking for as the first page to show the design idea.

Reason: At least the last couple of designs submitted understands it is a touch screen and the home page is not a web site home page. The reason I am still not able to select a design is that the quality of graphic design elements is sub par. For example, The treatment to the options for example are not sharp and up to mark.

Target Market(s)

Propective residents walking into a apartment leasing centers

Industry/Entity Type

Apartment

Requirements
Must have
• - Must have a design where the content, like name of the property, menu options and pictures, are dynamic. So for example, do not restrict the design in a manner that we cannot switch off an option without redesign of the page.
- Good use of icons for options
- Gives the user a calm and serene feeling while maintaining a crisp modern user interface
Nice to have
• - Design in a manner that the background can be a custom image for a specific client
- Description of animation on the screen where the images selected by the client can rotate/slide/appear/animate
Should not have
• - Boxy design
- Small options that cannot be touched by fingers
- dont plan on hover animations, will not work in touch

```html
<!DOCTYPE html>
<html lang="en">
<head>
<meta charset="utf-8">
<title>Fitness Center</title>
<link rel="stylesheet" href="https://fonts.googleapis.com/css2?family=Roboto+Condensed:wght@700&family=Roboto:wght@400;500;700&display=swap">
<style>
  :root {
    --bg: #3a7dcb;
    --bg-deep: #2f6db8;
    --top-light: #5b9ee2;
    --top-band: #3c7fcd;
    --tab: #3473bf;
    --tab-inner: #2d67b0;
    --sidebar: #4a8dd8;
    --sidebar-edge: #5c9ce2;
    --bottom-light: #4a92e0;
    --bottom-deep: #2f6ab6;
    --orb-light: #3fc0ec;
    --orb-deep: #0a78b8;
    --white: #ffffff;
    --text-soft: #e8f1fb;
  }
  * { box-sizing: border-box; margin: 0; padding: 0; }
  html, body { width: 1200px; height: 657px; overflow: hidden; }
  body {
    position: relative;
    background: linear-gradient(180deg, var(--bg) 0%, var(--bg-deep) 100%);
    font-family: "Roboto", Helvetica, Arial, sans-serif;
    color: var(--white);
  }
  .top-band {
    position: absolute; left: 0; top: 0; width: 1200px; height: 84px;
    background: linear-gradient(180deg, var(--top-light) 0%, #4f93da 52%, var(--top-band) 53%, #3576c3 100%);
    box-shadow: 0 2px 4px rgba(0,0,0,.15);
  }
  .title-tab {
    position: absolute; left: 461px; top: 0; width: 485px; height: 99px;
    background: linear-gradient(180deg, #3f80ca, var(--tab));
    border-radius: 0 0 6px 6px;
    box-shadow: 0 3px 8px rgba(0,0,0,.3);
  }
  .title-box {
    position: absolute; left: 22px; top: 31px; width: 437px; height: 44px;
    background: var(--tab-inner);
    border: 1px solid #5a94d6;
    display: flex; align-items: center; justify-content: center;
    font-family: "Roboto Condensed", "Arial Narrow", sans-serif;
    font-weight: 700; font-size: 25px; letter-spacing: .2px;
    text-shadow: 0 1px 2px rgba(0,0,0,.35);
    white-space: nowrap;
  }
  .sidebar {
    position: absolute; left: 0; top: 84px; width: 252px; height: 449px;
    background: linear-gradient(180deg, var(--sidebar) 0%, #3f84d2 100%);
    border-right: 1px solid var(--sidebar-edge);
  }
  .menu { list-style: none; position: absolute; left: 0; top: 0; width: 252px; }
  .menu-item {
    position: absolute; left: 49px; height: 24px;
    font-size: 16px; line-height: 24px; color: var(--text-soft);
    text-shadow: 0 1px 1px rgba(0,0,0,.2);
    white-space: nowrap;
  }
  .menu-item.active { font-size: 17.5px; color: var(--white); z-index: 2; }
  .active-pill { position: absolute; left: 27px; top: 121px; z-index: 1; }
  .photo-frame {
    position: absolute; left: 358px; top: 112px; width: 470px; height: 313px;
    background: var(--white); padding: 4px;
    box-shadow: 0 3px 10px rgba(0,0,0,.3);
  }
  .photo {
    width: 100%; height: 100%;
    background:
      linear-gradient(180deg, rgba(60,40,30,0) 0%, rgba(60,40,30,0) 55%, rgba(150,70,30,.6) 100%),
      linear-gradient(90deg, #6b5a4a 0%, #9a8a78 25%, #5d87c0 55%, #7fa6d4 75%, #b99a80 100%);
  }
  .nav-arrow { position: absolute; top: 243px; }
  .nav-arrow.prev { left: 317px; }
  .nav-arrow.next { left: 839px; }
  .feature-title {
    position: absolute; left: 902px; top: 134px;
    font-size: 28px; font-weight: 700; line-height: 34px;
  }
  .feature-text {
    position: absolute; left: 903px; top: 181px; width: 222px;
    font-size: 12.8px; line-height: 22px; color: var(--text-soft);
  }
  .bottom-band {
    position: absolute; left: 0; top: 533px; width: 1200px; height: 124px;
    background: linear-gradient(180deg, var(--bottom-light) 0%, #3b7dcb 45%, var(--bottom-deep) 100%);
    box-shadow: 0 -2px 4px rgba(0,0,0,.15) inset;
  }
  .option { position: absolute; top: 445px; width: 150px; height: 160px; text-align: center; }
  .option-cap {
    position: absolute; left: 7px; top: 0; width: 136px; height: 128px;
    border-radius: 68px 68px 0 0;
    background: linear-gradient(180deg, rgba(255,255,255,.18), rgba(90,150,220,.35));
    border: 1px solid rgba(255,255,255,.25); border-bottom: none;
  }
  .option-orb {
    position: absolute; left: 19px; top: 12px; width: 112px; height: 112px;
    border-radius: 50%;
    background: radial-gradient(circle at 50% 30%, var(--orb-light) 0%, #1a9bd6 50%, var(--orb-deep) 100%);
    border: 3px solid #2a8fd0;
    box-shadow: 0 4px 8px rgba(0,0,0,.35), inset 0 -6px 12px rgba(0,60,120,.35);
    display: flex; align-items: center; justify-content: center;
  }
  .option-orb::before {
    content: ""; position: absolute; left: 16px; top: 8px; width: 74px; height: 36px;
    border-radius: 50%; background: linear-gradient(180deg, rgba(255,255,255,.45), rgba(255,255,255,0));
  }
  .option-orb svg { position: relative; }
  .option-label {
    position: absolute; left: -20px; top: 130px; width: 190px;
    font-family: "Roboto Condensed", "Arial Narrow", sans-serif;
    font-weight: 700; font-size: 23px; letter-spacing: .2px;
    text-shadow: 0 1px 2px rgba(0,0,0,.35);
    white-space: nowrap;
  }
  .touch-hint {
    position: absolute; left: 578px; top: 618px; height: 36px;
    display: flex; align-items: center; gap: 8px;
    font-size: 16.5px; color: var(--white);
  }
</style>
</head>
<body>
  <header class="top-band"></header>
  <div class="title-tab"><div class="title-box">WHERE CONVENIENCE MEETS LUXURY</div></div>

  <nav class="sidebar">
    <svg class="active-pill" width="258" height="50" viewBox="0 0 258 50" aria-hidden="true">
      <defs>
        <linearGradient id="pillFill" x1="0" y1="0" x2="0" y2="1">
          <stop offset="0" stop-color="#6aa8e6"/><stop offset=".5" stop-color="#3b7cc8"/><stop offset="1" stop-color="#2a65b0"/>
        </linearGradient>
      </defs>
      <path d="M10 1 H228 L257 25 L228 49 H10 Q1 49 1 40 V10 Q1 1 10 1 Z" fill="url(#pillFill)" stroke="#7fb4ea" stroke-width="1"/>
    </svg>
    <ul class="menu">
      <li class="menu-item" style="top:45px">Site map</li>
      <li class="menu-item" style="top:89px">Swimming pool</li>
      <li class="menu-item active" style="top:133px">Fitness center</li>
      <li class="menu-item" style="top:177px">Tennis court</li>
      <li class="menu-item" style="top:221px">Play area</li>
      <li class="menu-item" style="top:265px">Gareges</li>
      <li class="menu-item" style="top:309px">Club House</li>
      <li class="menu-item" style="top:353px">Pets Area</li>
      <li class="menu-item" style="top:396px">Proximity to QUORLINE</li>
    </ul>
  </nav>

  <svg class="nav-arrow prev" width="31" height="51" viewBox="0 0 31 51" aria-label="Previous">
    <path d="M31 0 V51 L0 25.5 Z" fill="#5c9ce2"/><path d="M31 0 V25.5 H0 Z" fill="#8cc0f0"/>
  </svg>
  <div class="photo-frame">
    <div class="photo" role="img" aria-label="Photo of the fitness center: a long row of treadmills beside tall windows, wooden floor and lounge chairs"></div>
  </div>
  <svg class="nav-arrow next" width="31" height="51" viewBox="0 0 31 51" aria-label="Next">
    <path d="M0 0 V51 L31 25.5 Z" fill="#5c9ce2"/><path d="M0 0 V25.5 H31 Z" fill="#8cc0f0"/>
  </svg>

  <h1 class="feature-title">Fitness Center</h1>
  <p class="feature-text">Lorem Ipsum is simply dummy text of the printing and typesetting industry. Lorem Ipsum has been the industry's standard dummy text ever since the 1500s, when an unknown printer took a galley of type and scrambled it to make a type specimen book. It has survived not only five centuries, but also the leap into electronic</p>

  <footer class="bottom-band"></footer>

  <div class="option" style="left:297px">
    <div class="option-cap"></div>
    <div class="option-orb">
      <svg width="60" height="60" viewBox="0 0 60 60" fill="#fff" aria-hidden="true">
        <circle cx="30" cy="16" r="6"/><rect x="23" y="23" width="14" height="20" rx="3"/><rect x="25" y="40" width="4" height="16"/><rect x="31" y="40" width="4" height="16"/>
        <circle cx="13" cy="22" r="5"/><rect x="7" y="28" width="12" height="16" rx="3"/><rect x="9" y="42" width="3" height="12"/><rect x="14" y="42" width="3" height="12"/>
        <circle cx="47" cy="22" r="5"/><rect x="41" y="28" width="12" height="16" rx="3"/><rect x="43" y="42" width="3" height="12"/><rect x="48" y="42" width="3" height="12"/>
        <g stroke="#fff" stroke-width="2.5" stroke-linecap="round"><path d="M30 3v3M21 6l2 2.5M39 6l-2 2.5M16 11l2.5 1.5M44 11l-2.5 1.5"/></g>
      </svg>
    </div>
    <div class="option-label">COMMUNITY</div>
  </div>

  <div class="option" style="left:462px">
    <div class="option-cap"></div>
    <div class="option-orb">
      <svg width="72" height="62" viewBox="0 0 72 62" fill="#fff" aria-hidden="true">
        <path d="M36 4 L62 26 H56 V50 H16 V26 H10 Z"/>
        <rect x="32" y="36" width="9" height="14" fill="#1b98d4"/><rect x="23" y="28" width="8" height="7" fill="#1b98d4"/><rect x="43" y="28" width="8" height="7" fill="#1b98d4"/>
        <path d="M4 40 Q14 44 16 56 L8 58 Q6 48 2 44 Z"/><path d="M68 40 Q58 44 56 56 L64 58 Q66 48 70 44 Z"/>
      </svg>
    </div>
    <div class="option-label">NIGHBORHOOD</div>
  </div>

  <div class="option" style="left:628px">
    <div class="option-cap"></div>
    <div class="option-orb">
      <svg width="64" height="60" viewBox="0 0 64 60" fill="#fff" aria-hidden="true">
        <path d="M32 2 L60 16 H4 Z"/><rect x="6" y="18" width="52" height="4"/>
        <rect x="11" y="24" width="6" height="22"/><rect x="22" y="24" width="6" height="22"/><rect x="36" y="24" width="6" height="22"/><rect x="47" y="24" width="6" height="22"/>
        <rect x="6" y="48" width="52" height="4"/><rect x="2" y="54" width="60" height="5"/>
      </svg>
    </div>
    <div class="option-label">FLOOR PLANS</div>
  </div>

  <div class="option" style="left:795px">
    <div class="option-cap"></div>
    <div class="option-orb">
      <svg width="66" height="48" viewBox="0 0 66 48" aria-hidden="true">
        <rect x="2" y="2" width="62" height="44" rx="2" fill="#fff"/>
        <path d="M3 4 L33 28 L63 4" fill="none" stroke="#1b98d4" stroke-width="3"/>
        <path d="M3 45 L25 22 M63 45 L41 22" stroke="#1b98d4" stroke-width="2.5"/>
      </svg>
    </div>
    <div class="option-label">CONTACT US</div>
  </div>

  <div class="option" style="left:963px">
    <div class="option-cap"></div>
    <div class="option-orb">
      <svg width="56" height="70" viewBox="0 0 56 70" fill="#fff" aria-hidden="true">
        <path d="M16 12 Q18 2 30 3 Q40 4 41 12 Q34 8 26 12 Q20 14 16 12 Z"/>
        <path d="M4 66 Q4 38 22 32 L28 44 L34 32 Q52 38 52 66 Z"/>
      </svg>
    </div>
    <div class="option-label">COMPANY</div>
  </div>

  <div class="touch-hint">
    <svg width="22" height="36" viewBox="0 0 22 36" aria-hidden="true">
      <circle cx="9" cy="9" r="8" fill="none" stroke="#fff" stroke-width="1.5"/>
      <circle cx="9" cy="9" r="4" fill="none" stroke="#fff" stroke-width="1.5"/>
      <path d="M6 10 V24 L4 22 Q1 21 2 25 L8 34 H20 V21 Q20 18 17 18 L12 18 V10 Q12 7 9 7 Q6 7 6 10 Z" fill="#fff"/>
    </svg>
    <span>Touch an option to explore</span>
  </div>
</body>
</html>
```